Canadian Integrative health and wellness clinic needs a brochure

We need a tri-fold or bi-fold brochure to give out at marketing events and to prospective patients. We would like it to highlight our services offered and our philosophy of care. Please do not include staff profiles as these can change. We would like to give the impression of a cutting edge clinic, with the latest technologies and a patient centred approach.
Updates

Project Deadline Extended
Reason: There have been some excellent designs submitted so far. We have received notice from a few designers that they would like to submit more options in the next few days.

Target Market(s)

We are a clinic that works with families, athletes, seniors and anyone in between.

Industry/Entity Type

Health And Wellness

Font styles to use
Serif

Requirements
Must have
• Logo, info about our services offered, our philosophy of comprehensive treatments and patient centred care, location/contact info.
• I have high resolution images of any image found on our website if you wish to include any of those. www.brivonacare.ca
Nice to have
• colour scheme that includes blues and greys
• something that looks technologically advanced but year still clean and professional
Should not have
• individual staff names or bio's.

```html
<!DOCTYPE html>
<html lang="en">
<head>
<meta charset="utf-8">
<title>Brivona Care Brochure</title>
<link rel="stylesheet" href="https://fonts.googleapis.com/css2?family=Montserrat:wght@400;500;600;700&display=swap">
<style>
  :root{
    --page:#eceef1;
    --white:#ffffff;
    --royal:#0b5ea8;
    --royal-deep:#084b8c;
    --cyan:#00bdf2;
    --mid-blue:#1184d6;
    --head-blue:#0b68b0;
    --ink:#1e2226;
    --soft-grey:#d9dbde;
  }
  *{box-sizing:border-box;margin:0;padding:0}
  html,body{width:1200px;height:1200px;overflow:hidden}
  body{background:var(--page);font-family:"Montserrat",sans-serif;color:var(--ink);position:relative}
  .spread{position:absolute;left:200px;width:800px;height:564px;background:var(--white);box-shadow:0 10px 28px rgba(0,0,0,.18);overflow:hidden}
  .spread--outside{top:24px}
  .spread--inside{top:612px}
  .panel{position:absolute;top:0;height:564px}
  .panel--one{left:0;width:267px}
  .panel--two{left:267px;width:266px}
  .panel--three{left:533px;width:267px}
  .shapes{position:absolute;left:0;top:0;width:800px;height:564px;pointer-events:none}

  /* outside: pricing panel */
  .block{position:absolute;left:33px;width:212px;font-size:9.2px;line-height:1.28}
  .block--center{text-align:center}
  .heading-blue{color:var(--head-blue);font-weight:700;font-size:17px;letter-spacing:.3px;text-align:center}
  .link{color:var(--royal-deep);font-weight:600}
  .fine{font-size:8.4px;text-align:center}
  .insurers{position:absolute;left:30px;width:225px;top:423px;display:grid;grid-template-columns:1fr 1fr;column-gap:8px;font-size:8.2px;line-height:1.33;list-style:none}
  .insurers li::before{content:"• "}

  /* outside: contact panel */
  .panel--contact{background:linear-gradient(90deg,var(--royal-deep),var(--royal) 35%,#0c64b0);color:var(--white)}
  .contact-title{position:absolute;top:76px;width:100%;text-align:center;font-weight:600;font-size:16.5px;line-height:1.3;letter-spacing:.4px}
  .contact-list{position:absolute;top:148px;left:20px;right:12px;list-style:none;font-size:10.6px;font-weight:600}
  .contact-list li{display:flex;gap:8px;align-items:flex-start;margin-bottom:11.8px;line-height:1.25}
  .contact-list svg{flex:0 0 12px;width:12px;height:12px;margin-top:1px}
  .contact-note{display:block;font-weight:400;font-size:9.3px;margin-top:4px;line-height:1.2}
  .hours-title{position:absolute;top:459px;width:100%;text-align:center;font-weight:600;font-size:14.5px;letter-spacing:.4px}
  .hours{position:absolute;top:494px;width:100%;text-align:center;font-weight:600;font-size:12.8px;line-height:1.22}

  /* outside: cover panel */
  .cover-photo{position:absolute;inset:0;background:linear-gradient(180deg,#e9e8e6 0%,#dcdad6 35%,#c9c7c2 70%,#b9b6b1 100%)}
  .portrait{position:absolute;left:50px;top:160px;width:200px;height:404px;background:radial-gradient(ellipse at 50% 35%,#f2f2f0 0%,#e2e1de 60%,rgba(226,225,222,0) 75%)}
  .brand{position:absolute;top:40px;left:0;width:100%;text-align:center}
  .brand-name{display:inline-flex;align-items:center;gap:8px;font-weight:500;font-size:27px;color:var(--royal);letter-spacing:.5px}
  .brand-dot{width:12px;height:12px;border-radius:50%;background:var(--royal)}
  .brand-tag{margin-top:14px;font-size:7.3px;font-weight:500;color:var(--mid-blue)}

  /* inside: about panel */
  .about{position:absolute;left:22px;width:232px;font-size:8.7px;line-height:1.28;font-weight:500}
  .title-dark{font-weight:700;font-size:17.5px;color:#2a2d31}
  .title-dark .accent{color:var(--cyan)}
  .title-cyan{font-weight:700;font-size:16.5px;color:var(--cyan)}
  .about p{margin-top:3px}

  /* inside: services */
  .services-title{position:absolute;left:278px;top:30px;font-weight:700;font-size:20px;color:var(--head-blue);letter-spacing:.4px}
  .service{position:absolute;width:105px;text-align:center;font-size:9.6px;font-weight:600;color:#33373c;line-height:1.22}
  .service .thumb{display:block;width:105px;height:82px;margin-bottom:6px}
  .fold-shade{position:absolute;left:533px;top:0;width:120px;height:564px;background:linear-gradient(90deg,rgba(0,0,0,.07),rgba(0,0,0,0))}
  .fold-shade--left{left:267px;width:60px;background:linear-gradient(90deg,rgba(0,0,0,.1),rgba(0,0,0,0))}
</style>
</head>
<body>

<section class="spread spread--outside">
  <div class="panel panel--one">
    <h2 class="heading-blue" style="position:absolute;top:100px;width:100%">PRICING</h2>
    <p class="block block--center" style="top:129px;font-size:10px">For updated services pricing,<br>please visit:<br><span class="link">www.brivonacare.ca/Pricing/</span></p>
    <p class="block" style="top:185px">We also custom order various othopedic supports and supplies. Examples are knee braces, ankle braces, back supports, orthopedic pillows and various other supplies. Please contact us if you have a specific request.</p>
    <p class="block fine" style="top:262px">All prices include GST (where applicable)</p>

    <h2 class="heading-blue" style="position:absolute;top:300px;width:100%">DIRECT BILLING</h2>
    <p class="block" style="top:327px">We offer direct billing to most extended healthcare plans. As all insurance companies and plans are different, we recommend asking your plan provider directly if they allow direct billing on your specific plan. The following insurance companies typically allow direct billing:</p>
    <ul class="insurers">
      <li>Northgate Health</li><li>Halvern</li>
      <li>Maple Benefit Co.</li><li>Halvern Group</li>
      <li>Corwin Mutual</li><li>Meridian Life</li>
      <li>Laurier Trust</li><li>Keystone Benefit</li>
      <li>Prairie West Life</li><li>Lakeshore Life</li>
      <li>Summit Financial</li><li>Solstice Life</li>
    </ul>
    <p class="block" style="top:497px">If you were involved in a motor vehicle accident, we are likely able to direct bill for your treatment. Please <strong>contact us</strong> for more information.</p>
  </div>

  <div class="panel panel--two panel--contact">
    <h2 class="contact-title">WE WOULD LOVE<br>TO HEAR FROM YOU!</h2>
    <ul class="contact-list">
      <li><svg viewBox="0 0 12 12" aria-hidden="true"><path fill="var(--cyan)" d="M2.4 1l2 2.3-1 1.3c.8 1.6 1.8 2.6 3.3 3.3l1.3-1L10.8 9 9.6 10.8C5.2 10.5 1.5 6.8 1.2 2.4z"/></svg>(403) 555-0147</li>
      <li><svg viewBox="0 0 12 12" aria-hidden="true"><rect x="1" y="1.5" width="10" height="9" rx="1" fill="var(--cyan)"/></svg>www.brivonacare.ca</li>
      <li><svg viewBox="0 0 12 12" aria-hidden="true"><rect x="1" y="2.5" width="10" height="7" rx="1" fill="var(--cyan)"/><path d="M1.5 3.2 6 6.6l4.5-3.4" fill="none" stroke="var(--royal)" stroke-width="1"/></svg>info@brivonacare.ca</li>
      <li><svg viewBox="0 0 12 12" aria-hidden="true"><circle cx="6" cy="6" r="5" fill="var(--cyan)"/></svg>fb.com/brivonacarewellness</li>
      <li><svg viewBox="0 0 12 12" aria-hidden="true"><circle cx="6" cy="6" r="5" fill="var(--cyan)"/></svg>@brivona_care</li>
      <li><svg viewBox="0 0 12 12" aria-hidden="true"><path fill="var(--cyan)" d="M6 .8a3.8 3.8 0 0 1 3.8 3.8C9.8 7.3 6 11.2 6 11.2S2.2 7.3 2.2 4.6A3.8 3.8 0 0 1 6 .8zm0 2.3a1.5 1.5 0 1 0 0 3 1.5 1.5 0 0 0 0-3z"/></svg>
        <span>1480 Marlow Ridge Way NW,<br>Suite 310 Calgary, Alberta T3P 2K7
          <span class="contact-note">We are located in Lindenvale Town Square, next to the Harvest Grocer and above the main floor medical clinics.</span></span></li>
    </ul>
    <h2 class="hours-title">CLINIC HOURS</h2>
    <p class="hours">Monday - &nbsp;Friday 8am - 8pm<br>Saturday - 9am - 5pm<br>Sunday - Closed</p>
  </div>

  <div class="panel panel--three">
    <div class="cover-photo" role="img" aria-label="Bright clinic interior with a smiling practitioner in a white uniform, arms crossed"></div>
    <div class="portrait" aria-hidden="true"></div>
    <div class="brand">
      <div class="brand-name"><span class="brand-dot"></span>Brivona Care</div>
      <div class="brand-tag">Chiropractic • Massage Therapy • Acupuncture • Shockwave • Laser</div>
    </div>
  </div>

  <svg class="shapes" viewBox="0 0 800 564" aria-hidden="true">
    <polygon points="0,0 142,0 0,81" fill="var(--mid-blue)"/>
    <polygon points="142,0 260,139 48,52" fill="var(--cyan)"/>
    <polygon points="430,382 533,428 533,492" fill="var(--cyan)"/>
  </svg>
</section>

<section class="spread spread--inside">
  <div class="panel panel--one">
    <div class="about" style="top:90px">
      <h2 class="title-dark">ABOUT <span class="accent">US</span></h2>
      <p>Brivona Care is NW Calgary's most comprehensive approach to living well. We are an owner-operated, multi-disciplinary clinic that uses a patient centred, evidence informed approach to help our patients move better, feel better and live better. We are located just north off Harrow Trail in Lindenvale, one of NW Calgary's newest and largest communities.</p>
    </div>
    <div class="about" style="top:230px">
      <h2 class="title-cyan">MISSION</h2>
      <p>To provide effective, efficient and thorough health services to help our patients achieve their highest level of health and wellbeing.</p>
    </div>
    <div class="about" style="top:315px">
      <h2 class="title-cyan" style="line-height:1.2">PERSONAL INFORMATION<br><span style="color:#2a2d31">AND PRIVACY</span></h2>
      <p>Brivona Care is committed to building relationships with our patients. These relationships are built on trust and respect. Part of how we establish trust and respect with you is by telling you what information we require from you, how this information will be handled, and how this information will be kept safe. We know that the privacy of your personal information is very important and we want you to know that we take privacy very seriously.</p>
      <p style="margin-top:9px">The Brivona Care Privacy Policy explains the types of personal information we collect, how it is used, and the steps we take to ensure your personal information is handled appropriately.</p>
    </div>
  </div>

  <div class="fold-shade fold-shade--left" aria-hidden="true"></div>
  <div class="fold-shade" aria-hidden="true"></div>

  <h2 class="services-title">SERVICES</h2>

  <div class="service" style="left:278px;top:67px"><span class="thumb" role="img" aria-label="Chiropractor's hands adjusting a patient's back" style="background:linear-gradient(160deg,#c7a58f,#6f7f92)"></span>CHIROPRACTIC</div>
  <div class="service" style="left:408px;top:67px"><span class="thumb" role="img" aria-label="Therapist massaging a client's shoulders" style="background:linear-gradient(160deg,#3a3a3c,#c99b7e)"></span>MASSAGE</div>
  <div class="service" style="left:537px;top:67px"><span class="thumb" role="img" aria-label="Acupuncture needles placed along a patient's skin" style="background:linear-gradient(160deg,#d4a894,#b9473f 60%,#e2c2b2)"></span>ACUPUNCTURE</div>
  <div class="service" style="left:667px;top:67px"><span class="thumb" role="img" aria-label="Shockwave device applied to a patient's shoulder" style="background:linear-gradient(160deg,#e8e6e4,#c98f73 55%,#3c3d40)"></span>SHOCKWAVE</div>

  <div class="service" style="left:278px;top:180px"><span class="thumb" role="img" aria-label="Laser therapy probe held against a knee" style="background:linear-gradient(160deg,#3b3d42,#e4e4e6 50%,#c9a08a)"></span>LASER THERAPHY</div>
  <div class="service" style="left:408px;top:180px"><span class="thumb" role="img" aria-label="Practitioner performing release work on a patient's arm" style="background:linear-gradient(160deg,#e6e4e0,#9aa1a8 50%,#2f3136)"></span>ACTIVE RELEASE</div>
  <div class="service" style="left:537px;top:180px"><span class="thumb" role="img" aria-label="Pink and blue kinesiology tape on a calf" style="background:linear-gradient(100deg,#f0a8b6,#5ab8e0 50%,#e9d3c5)"></span>KINSEOLOGY TAPE</div>
  <div class="service" style="left:667px;top:180px"><span class="thumb" role="img" aria-label="Steel soft-tissue tool on a patient's shoulder" style="background:linear-gradient(160deg,#4a3a33,#b07b63 55%,#2b2a2a)"></span>TOOL-GLIDE<br>TECHNIQUE</div>

  <div class="service" style="left:278px;top:306px"><span class="thumb" role="img" aria-label="Glass cupping treatment on skin" style="background:linear-gradient(160deg,#f2e2d4,#d9a585 55%,#f4ede6)"></span>CUPPING<br>TECHNIQUE</div>
  <div class="service" style="left:408px;top:306px"><span class="thumb" role="img" aria-label="Hot stones placed along a client's back" style="background:linear-gradient(160deg,#2a211c,#b9774f 55%,#5a3a27)"></span>HOT/COLD STONE<br>MASSAGE</div>
  <div class="service" style="left:537px;top:306px"><span class="thumb" role="img" aria-label="Runner on a sunny path at sunset" style="background:linear-gradient(180deg,#f4eedc,#c9c08e 60%,#8f8a5a)"></span>WEIGHT LOSS<br>MGMT. PROGRAM</div>

  <svg class="shapes" viewBox="0 0 800 564">
    <polygon points="0,0 268,0 107,24 0,76" fill="var(--mid-blue)" aria-hidden="true"/>
    <polygon points="107,24 268,0 268,96" fill="var(--cyan)" aria-hidden="true"/>
    <polygon points="267,478 267,564 382,564" fill="var(--mid-blue)" aria-hidden="true"/>
    <polygon points="519,414 420,564 292,564" fill="var(--cyan)" aria-hidden="true"/>
    <polygon points="519,414 800,466 800,564 407,564" fill="#8d8479" role="img" aria-label="Clinic reception area with waiting chairs and front desk"/>
    <polygon points="519,414 800,466 800,500 470,500" fill="#b5aca0" aria-hidden="true"/>
  </svg>
</section>

</body>
</html>
```